hair salon logo and Business Card Design

this logo needs to reflect a vibrant, trendy and fun business, targeting 20 to 50 year old ladies in a nice sunny part of Australia.Our aim is to make everyone feel in a fantastic mood when they walk out of the salon,and look equally glamorous.
I would like the logo to be simple yet using bold colors and font.
ideally the name mira would be lowercase with a nice rounded shape and hair+beauty, with upper case and the letter i in an inverted position.

Industry/Entity Type

Hair

Contact Information for Business Card

mira
hair | beauty.

Lina Fosterby
stylist/owner
0471590263
48 Pellow St. Larkhaven NSR. 7031

Requirements
Must have
• front all the business details
back lined for writing notes.
Nice to have
• use of bold stand out colors, simple shapes sense of movement, not stillness, modern, professional.

```html
<!DOCTYPE html>
<html lang="en">
<head>
<meta charset="utf-8">
<title>mira hair | beauty – business cards</title>
<link rel="stylesheet" href="https://fonts.googleapis.com/css2?family=Arimo:wght@400&family=Cousine:wght@700&family=Tinos:wght@700&display=swap">
<style>
  :root {
    --backdrop: #eceeed;
    --card-rose: #d86b96;
    --card-blush: #e9a9c3;
    --panel-blush: #e8bacd;
    --band-light: rgba(255, 235, 243, 0.75);
    --ink-white: #ffffff;
    --ink-teal: #1f5152;
    --mark-red: #d9363e;
  }
  * { box-sizing: border-box; margin: 0; padding: 0; }
  html, body { width: 1200px; height: 798px; overflow: hidden; }
  body {
    background: var(--backdrop);
    position: relative;
  }
  .card {
    position: absolute;
    top: 256px;
    width: 510px;
    height: 286px;
    border-radius: 3px;
    overflow: hidden;
  }
  .card--details { left: 60px; background: var(--card-rose); }
  .card--brand { left: 630px; background: var(--card-blush); }

  .sheen-band {
    position: absolute;
    left: 0; right: 0;
    top: 118px;
    height: 22px;
    background: linear-gradient(90deg, transparent 0%, var(--band-light) 45%, var(--band-light) 60%, transparent 100%);
  }
  .card--details .sheen-band { left: 160px; right: 30px; }

  .holder {
    position: absolute;
    left: 40px;
    top: 150px;
    color: var(--ink-white);
  }
  .holder__name {
    font-family: "Tinos", "Times New Roman", serif;
    font-weight: 700;
    font-size: 24px;
    letter-spacing: 0.5px;
  }
  .holder__role {
    font-family: "Arimo", Arial, sans-serif;
    font-size: 12px;
    margin-top: 6px;
  }
  .contact {
    position: absolute;
    right: 32px;
    top: 150px;
    text-align: right;
    font-family: "Cousine", "Courier New", monospace;
    font-weight: 700;
    font-size: 13px;
    line-height: 17px;
    color: var(--ink-white);
    font-style: normal;
  }

  .brand-panel {
    position: absolute;
    inset: 22px 22px;
    background: var(--panel-blush);
  }
  .brand-panel .sheen-band { top: 108px; left: 40px; right: 40px; }
  .brand-mark {
    position: absolute;
    left: 50%;
    top: 50%;
    transform: translate(-50%, -50%);
    display: flex;
    align-items: center;
    gap: 14px;
  }
  .brand-mark__dot {
    width: 40px;
    height: 40px;
    border-radius: 50%;
    background: var(--mark-red);
  }
  .brand-mark__name {
    font-family: "Tinos", "Times New Roman", serif;
    font-weight: 700;
    font-size: 64px;
    line-height: 1;
    color: var(--ink-teal);
  }
</style>
</head>
<body>
  <section class="card card--details" aria-label="Business card, contact side">
    <div class="sheen-band"></div>
    <div class="holder">
      <p class="holder__name">Lina Fosterby</p>
      <p class="holder__role">Stylist/Owner</p>
    </div>
    <address class="contact">
      Tel: 0471590263<br>
      48 Pellow<br>
      St. Larkhaven<br>
      NSR. 7031
    </address>
  </section>

  <section class="card card--brand" aria-label="Business card, brand side">
    <div class="brand-panel">
      <div class="sheen-band"></div>
      <div class="brand-mark">
        <span class="brand-mark__dot"></span>
        <span class="brand-mark__name">mira</span>
      </div>
    </div>
  </section>
</body>
</html>
```